Verdant Tide Collective needs packaging design for 500g Hemp Seed Pouch

We need a packaging design for the release of our Australian sourced Super Healthy, Nutritious super food HEMP SEED.

The verdant Tide collective - food, fibre, fuel, building, medicine
We are a start up company who is very Passionate about Hemp, rebuilding the hemp industry through inspiration, education and distribution of all things hemp.

This Hemp Seed packaging will be our first product launch

Kernel of NUVA GRAINS 500gram

needs to communicate 3 things, that Hemp seeds:
1. TASTE GREAT
2. EASY TO USE
3. GOOD FOR YOU

other Features of hemp seeds is that they are :
Vegan
Paleo
Raw
Sustainable
High in protein
High in Omega 3 + 6 EFA
Anti allergenic

we would like to see designs that work with our current logo and colouring of orange and black. premium and stylish that says healthy

the pouches will be '500g' meaning they will hold 500grams of hulled hemp seeds.

with dimensions of
170mm x 250mm
see attached photo of competitors hemp protein pouch as example of pouch design

see attached for current logo designs and colouring
also see attached concept sketch we are not married to this sketch it is just as a guideline for elements that should be included.

final design should feel healthy clean and safe for consumption:)
with an emphasis on being PremiumAustralian seed soured from from pristine Tasmania

Health conscious

• map of Australia or show that it is Australian in some way
• Spoon of hemp seeds or picture of Nuva Kernels

```html
<!DOCTYPE html>
<html lang="en">
<head>
<meta charset="utf-8">
<title>Verdant Tide Collective – Hemp Seed 500 gm Pouch</title>
<link href="https://fonts.googleapis.com/css2?family=Archivo+Black&family=Fjalla+One&family=Montserrat:wght@500;700;800&display=swap" rel="stylesheet">
<style>
  :root{
    --orange:#f7901e;
    --orange-deep:#f08a1c;
    --peach:#fbc592;
    --ink:#1e1e1e;
    --leaf:#8cc63f;
    --forest:#3b6b2a;
    --forest-dark:#2f5a22;
    --white:#ffffff;
  }
  *{box-sizing:border-box;margin:0;padding:0}
  html,body{width:820px;height:1200px;overflow:hidden;background:var(--peach)}
  .pouch{position:relative;width:820px;height:1200px;overflow:hidden;font-family:"Fjalla One",sans-serif;color:var(--ink)}
  .sunburst{position:absolute;inset:0;background:radial-gradient(circle at 50% 55%,#fcd3a8 0%,var(--peach) 35%,#f8a95a 75%,var(--orange) 100%)}
  .tag{position:absolute;left:295px;top:0;width:220px;height:258px;background:var(--orange);box-shadow:0 3px 6px rgba(0,0,0,.25)}
  .tag-stitch{position:absolute;left:12px;right:12px;top:-4px;bottom:14px;border:2px dashed var(--white);border-top:none;border-radius:0 0 14px 14px}
  .brand-mark{position:absolute;display:flex;align-items:center;justify-content:center;text-align:center;border-radius:50%;background:var(--orange-deep)}
  .brand-mark span{font-family:"Montserrat",sans-serif;font-weight:800;color:var(--ink);line-height:1.05;text-transform:lowercase}
  .brand-mark--tag{left:332px;top:45px;width:154px;height:154px}
  .brand-mark--tag span{font-size:22px}
  .brand-mark--hero{left:291px;top:535px;width:236px;height:236px;box-shadow:0 4px 10px rgba(0,0,0,.25)}
  .brand-mark--hero span{font-size:34px}
  .product-title{position:absolute;left:0;width:820px;top:282px;text-align:center;font-family:"Archivo Black",sans-serif;font-size:104px;line-height:1;color:var(--leaf);-webkit-text-stroke:5px var(--ink);paint-order:stroke fill;letter-spacing:-1px}
  .collective-box{position:absolute;left:150px;top:425px;width:520px;height:98px;background:var(--white);border:3px solid var(--orange);border-radius:12px;text-align:center;box-shadow:0 3px 5px rgba(0,0,0,.2)}
  .collective-name{font-family:"Montserrat",sans-serif;font-weight:800;font-size:34px;margin-top:8px;letter-spacing:-.5px}
  .collective-name .accent{color:var(--orange)}
  .collective-pillars{font-family:"Montserrat",sans-serif;font-weight:500;font-size:20px;margin-top:4px}
  .features{position:absolute;list-style:none}
  .features--left{left:134px;top:555px}
  .features--right{left:547px;top:555px}
  .feature{display:flex;align-items:flex-start;height:78px}
  .feature svg{flex:none;width:56px;height:50px}
  .feature-label{margin-left:12px;margin-top:8px;font-size:20px;line-height:1.25;text-transform:uppercase;letter-spacing:.5px}
  .contents-bar{position:absolute;left:212px;top:822px;width:393px;height:48px;background:var(--forest);border-radius:10px;color:var(--white);text-align:center;font-size:24px;line-height:48px;letter-spacing:1px}
  .nutrients{position:absolute;left:218px;top:884px;display:flex;gap:11px}
  .nutrient{position:relative;width:88px;height:108px}
  .nutrient svg{position:absolute;inset:0}
  .nutrient-value{position:absolute;left:0;right:0;top:12px;text-align:center;font-size:23px}
  .nutrient-name{position:absolute;left:0;right:0;top:64px;text-align:center;font-size:13px;color:var(--white);letter-spacing:.5px;text-transform:uppercase}
  .weight{position:absolute;left:0;width:820px;top:1012px;text-align:center;font-size:23px}
  .origin{position:absolute;left:122px;top:1030px;display:flex;align-items:center}
  .flag-badge{width:68px;height:68px;border-radius:50%;background:radial-gradient(circle at 40% 40%,#2d4aa8,#12256e);box-shadow:0 2px 4px rgba(0,0,0,.3)}
  .origin-text{margin-left:12px;font-size:18px;letter-spacing:.2px}
</style>
</head>
<body>
<main class="pouch">
  <div class="sunburst" role="img" aria-label="Orange and peach sunburst rays radiating from the centre"></div>

  <div class="tag"><div class="tag-stitch"></div></div>
  <div class="brand-mark brand-mark--tag"><span>verdant<br>tide<br>collective</span></div>

  <h1 class="product-title">Hemp Seed</h1>

  <section class="collective-box">
    <p class="collective-name">verdant <span class="accent">tide</span> collective</p>
    <p class="collective-pillars">Food &bull; Fibre &bull; Fuel &bull; Building &bull; Medicine</p>
  </section>

  <div class="brand-mark brand-mark--hero"><span>verdant<br>tide<br>collective</span></div>

  <ul class="features features--left">
    <li class="feature"><svg viewBox="0 0 56 50"><circle cx="24" cy="26" r="21" fill="#6cae3a" stroke="#fff" stroke-width="4"/><path d="M13 26l9 9 26-30" fill="none" stroke="#fff" stroke-width="6" stroke-linecap="round" stroke-linejoin="round"/></svg><span class="feature-label">Raw</span></li>
    <li class="feature"><svg viewBox="0 0 56 50"><circle cx="24" cy="26" r="21" fill="#6cae3a" stroke="#fff" stroke-width="4"/><path d="M13 26l9 9 26-30" fill="none" stroke="#fff" stroke-width="6" stroke-linecap="round" stroke-linejoin="round"/></svg><span class="feature-label">Paleo</span></li>
    <li class="feature"><svg viewBox="0 0 56 50"><circle cx="24" cy="26" r="21" fill="#6cae3a" stroke="#fff" stroke-width="4"/><path d="M13 26l9 9 26-30" fill="none" stroke="#fff" stroke-width="6" stroke-linecap="round" stroke-linejoin="round"/></svg><span class="feature-label">High in<br>Protein</span></li>
  </ul>
  <ul class="features features--right">
    <li class="feature"><svg viewBox="0 0 56 50"><circle cx="24" cy="26" r="21" fill="#6cae3a" stroke="#fff" stroke-width="4"/><path d="M13 26l9 9 26-30" fill="none" stroke="#fff" stroke-width="6" stroke-linecap="round" stroke-linejoin="round"/></svg><span class="feature-label">Vegan</span></li>
    <li class="feature"><svg viewBox="0 0 56 50"><circle cx="24" cy="26" r="21" fill="#6cae3a" stroke="#fff" stroke-width="4"/><path d="M13 26l9 9 26-30" fill="none" stroke="#fff" stroke-width="6" stroke-linecap="round" stroke-linejoin="round"/></svg><span class="feature-label">Anti Allergenic</span></li>
    <li class="feature"><svg viewBox="0 0 56 50"><circle cx="24" cy="26" r="21" fill="#6cae3a" stroke="#fff" stroke-width="4"/><path d="M13 26l9 9 26-30" fill="none" stroke="#fff" stroke-width="6" stroke-linecap="round" stroke-linejoin="round"/></svg><span class="feature-label">High in Omega<br>3+6 EFA</span></li>
  </ul>

  <div class="contents-bar">20 GRAM HEMP SEED CONTAINS</div>

  <div class="nutrients">
    <div class="nutrient"><svg viewBox="0 0 88 108"><path d="M8 4h72v84l-36 16-36-16z" fill="#3b6b2a" stroke="#2f5a22" stroke-width="4" stroke-linejoin="round"/><rect x="13" y="9" width="62" height="42" fill="#fff"/><line x1="18" y1="49" x2="70" y2="49" stroke="#3b6b2a" stroke-width="2"/></svg><span class="nutrient-value">2.0 G</span><span class="nutrient-name">Omega3</span></div>
    <div class="nutrient"><svg viewBox="0 0 88 108"><path d="M8 4h72v84l-36 16-36-16z" fill="#3b6b2a" stroke="#2f5a22" stroke-width="4" stroke-linejoin="round"/><rect x="13" y="9" width="62" height="42" fill="#fff"/><line x1="18" y1="49" x2="70" y2="49" stroke="#3b6b2a" stroke-width="2"/></svg><span class="nutrient-value">6.4 G</span><span class="nutrient-name">Protein</span></div>
    <div class="nutrient"><svg viewBox="0 0 88 108"><path d="M8 4h72v84l-36 16-36-16z" fill="#3b6b2a" stroke="#2f5a22" stroke-width="4" stroke-linejoin="round"/><rect x="13" y="9" width="62" height="42" fill="#fff"/><line x1="18" y1="49" x2="70" y2="49" stroke="#3b6b2a" stroke-width="2"/></svg><span class="nutrient-value">2.1 MG.</span><span class="nutrient-name">Iron</span></div>
    <div class="nutrient"><svg viewBox="0 0 88 108"><path d="M8 4h72v84l-36 16-36-16z" fill="#3b6b2a" stroke="#2f5a22" stroke-width="4" stroke-linejoin="round"/><rect x="13" y="9" width="62" height="42" fill="#fff"/><line x1="18" y1="49" x2="70" y2="49" stroke="#3b6b2a" stroke-width="2"/></svg><span class="nutrient-value">128 MG.</span><span class="nutrient-name">Magnesium</span></div>
  </div>

  <p class="weight">500 gm.</p>

  <div class="origin">
    <div class="flag-badge" role="img" aria-label="Round Australian flag badge"></div>
    <p class="origin-text">Premium Australian seed sourced from pristine Tasmania</p>
  </div>
</main>
</body>
</html>
```